ashby paving works

Needs to have phone number 0412885107 and email marklowry@pavemail.com.au.
ABN 27613048852
name mark lowry

For all your concreting solutions
Excavation
Exposed & colour concrete
House & shed slabs
Driveways
Landing & steps

Contact Information for Business Card

ph 0412885107
email marklowry@pavemail.com.au.
ABN 27613048852
name mark lowry

```html
<!DOCTYPE html>
<html lang="en">
<head>
<meta charset="utf-8">
<title>Ashby Paving Works – Business Card</title>
<link href="https://fonts.googleapis.com/css2?family=Lato:wght@400;700&display=swap" rel="stylesheet">
<style>
  :root {
    --orange: #f26a24;
    --charcoal: #666666;
    --white: #ffffff;
    --backdrop: #e6e7e8;
    --marker: #6b6b6b;
  }
  * { margin: 0; padding: 0; box-sizing: border-box; }
  html, body {
    width: 1200px; height: 1000px; overflow: hidden;
    background: var(--backdrop);
    font-family: "Lato", sans-serif;
  }
  .card {
    position: absolute; left: 278px; width: 644px; height: 393px;
    background: var(--white); overflow: hidden;
  }
  .card--front { top: 75px; }
  .card--back { top: 532px; }
  .top-band { position: absolute; left: 0; top: 0; width: 100%; height: 30px; background: var(--orange); }

  .brand { position: absolute; left: 0; width: 100%; }
  .brand__square { position: absolute; background: var(--orange); }
  .brand__divider { position: absolute; width: 2px; background: var(--orange); }
  .brand__name {
    position: absolute; color: var(--orange); font-weight: 700;
    white-space: nowrap; letter-spacing: 0.2px;
  }
  .brand__phone {
    position: absolute; color: var(--orange); font-weight: 400;
    letter-spacing: 1.5px; white-space: nowrap;
  }

  /* front */
  .card--front .brand__square { left: 150px; top: 86px; width: 62px; height: 62px; }
  .card--front .brand__divider { left: 247px; top: 63px; height: 102px; }
  .card--front .brand__name { left: 258px; top: 84px; font-size: 22px; }
  .card--front .brand__phone { left: 323px; top: 121px; font-size: 16px; }

  .contact-panel {
    position: absolute; left: 0; top: 196px; width: 100%; height: 197px;
    background: var(--charcoal);
  }
  .contact-panel__name {
    position: absolute; left: 64px; top: 62px;
    color: var(--orange); font-size: 21px; font-weight: 700;
  }
  .contact-list {
    position: absolute; left: 249px; top: 64px;
    display: grid; grid-template-columns: 76px auto;
    row-gap: 1px; color: var(--white); font-size: 19px; line-height: 23px;
  }

  /* back */
  .card--back .brand__square { left: 176px; top: 56px; width: 42px; height: 42px; }
  .card--back .brand__divider { left: 249px; top: 41px; height: 74px; }
  .card--back .brand__name { left: 257px; top: 57px; font-size: 15px; }
  .card--back .brand__phone { left: 305px; top: 84px; font-size: 12px; letter-spacing: 1.2px; }

  .services-panel {
    position: absolute; left: 0; top: 127px; width: 100%; height: 266px;
    background: var(--orange);
  }
  .services { position: absolute; top: 52px; list-style: none; }
  .services--left { left: 75px; width: 240px; }
  .services--right { left: 367px; width: 240px; }
  .services li {
    position: relative; color: var(--white); font-size: 21px; line-height: 27px;
    margin-bottom: 15px;
  }
  .services li::before {
    content: ""; position: absolute; left: -22px; top: 7px;
    border-left: 7px solid var(--marker);
    border-top: 6px solid transparent; border-bottom: 6px solid transparent;
  }
</style>
</head>
<body>

<section class="card card--front">
  <div class="top-band"></div>
  <div class="brand">
    <span class="brand__square"></span>
    <span class="brand__divider"></span>
    <span class="brand__name">ASHBY PAVING WORKS</span>
    <span class="brand__phone">0412885107</span>
  </div>
  <div class="contact-panel">
    <p class="contact-panel__name">Mark Lowry</p>
    <div class="contact-list">
      <span>Mobile</span><span>0412 885 107</span>
      <span>Email</span><span>marklowry@pavemail.com.au</span>
      <span>ABN</span><span>27 613 048 852</span>
    </div>
  </div>
</section>

<section class="card card--back">
  <div class="top-band"></div>
  <div class="brand">
    <span class="brand__square"></span>
    <span class="brand__divider"></span>
    <span class="brand__name">ASHBY PAVING WORKS</span>
    <span class="brand__phone">0412885107</span>
  </div>
  <div class="services-panel">
    <ul class="services services--left">
      <li>For all your concreting solutions</li>
      <li>Excavation</li>
      <li>Exposed &amp; colour concrete</li>
    </ul>
    <ul class="services services--right">
      <li>House &amp; shed slabs</li>
      <li>Driveways</li>
      <li>Landing &amp; steps</li>
    </ul>
  </div>
</section>

</body>
</html>
```